The Perfect Business Card for PineHarbor

I am looking for a business card which beautifully incorporates my logo, reflects my business and looks special, elegant and clean.

```html
<!DOCTYPE html>
<html lang="en">
<head>
<meta charset="utf-8">
<title>PineHarbor Business Card</title>
<link href="https://fonts.googleapis.com/css2?family=Montserrat:wght@400;500;700&display=swap" rel="stylesheet">
<style>
  :root {
    --brand-green: #7a9b43;
    --brand-green-dark: #6a8a36;
    --paper: #ffffff;
    --ink: #1c1c1c;
    --backdrop: #e6e6e6;
  }
  * { margin: 0; padding: 0; box-sizing: border-box; }
  html, body { width: 1200px; height: 856px; overflow: hidden; }
  body {
    background: var(--backdrop);
    font-family: "Montserrat", sans-serif;
    display: flex;
    align-items: center;
    justify-content: center;
    gap: 40px;
  }
  .card {
    width: 540px;
    height: 309px;
    position: relative;
    overflow: hidden;
    box-shadow: 0 6px 18px rgba(0,0,0,0.18);
  }

  /* Front */
  .card-front { background: var(--paper); }
  .front-logo {
    position: absolute;
    top: 52px; left: 0; right: 0;
    display: flex; align-items: center; justify-content: center; gap: 12px;
  }
  .logo-dot {
    width: 46px; height: 46px; border-radius: 50%;
    border: 2px solid var(--brand-green);
  }
  .logo-name {
    font-weight: 500;
    font-size: 40px;
    letter-spacing: 1px;
    color: var(--brand-green);
  }
  .front-details {
    position: absolute;
    top: 138px; left: 0; right: 0;
    display: flex; justify-content: center; align-items: center;
  }
  .person { text-align: right; padding-right: 18px; }
  .person-name {
    font-weight: 700; font-size: 19px; color: var(--brand-green); letter-spacing: 0.5px;
  }
  .person-role { font-size: 18px; color: var(--ink); margin-top: 2px; }
  .divider { width: 1.5px; height: 74px; background: var(--brand-green); }
  .contacts { list-style: none; padding-left: 16px; }
  .contacts li {
    display: flex; align-items: center; gap: 8px;
    font-size: 13px; color: var(--ink); line-height: 22px;
  }
  .contacts svg { width: 13px; height: 13px; fill: var(--brand-green); flex: none; }
  .address-band {
    position: absolute;
    left: 0; right: 0; bottom: 28px; height: 40px;
    background: var(--brand-green);
    color: var(--paper);
    font-size: 13.5px; font-weight: 500;
    display: flex; align-items: center; justify-content: center;
    letter-spacing: 0.3px;
  }

  /* Back */
  .card-back { background: var(--brand-green); }
  .world-pattern {
    position: absolute; inset: 30px 40px;
    background: radial-gradient(ellipse at center, rgba(255,255,255,0.10), rgba(255,255,255,0) 70%);
  }
  .back-logo {
    position: absolute; inset: 0;
    display: flex; align-items: center; justify-content: center; gap: 14px;
  }
  .back-logo .logo-dot { border-color: var(--paper); width: 54px; height: 54px; }
  .back-logo .logo-name { color: var(--paper); font-size: 44px; }
</style>
</head>
<body>
  <section class="card card-front">
    <div class="front-logo">
      <span class="logo-dot"></span>
      <span class="logo-name">PineHarbor</span>
    </div>
    <div class="front-details">
      <div class="person">
        <p class="person-name">DARA WELLINGTON</p>
        <p class="person-role">Co-Founder</p>
      </div>
      <div class="divider"></div>
      <ul class="contacts">
        <li>
          <svg viewBox="0 0 16 16"><path d="M3.2 1.5l2.4 2.6-1.3 1.8c.9 2 2.6 3.7 4.6 4.6l1.8-1.3 2.6 2.4-1.2 2.4C7 13.6 2.4 9 1.5 3.5z"/></svg>
          (555) 214-7730
        </li>
        <li>
          <svg viewBox="0 0 16 16"><path d="M1 3h14v10H1z M1.5 3.5L8 9l6.5-5.5" stroke="#fff" stroke-width="1.2"/></svg>
          info@pineharbor.com
        </li>
        <li>
          <svg viewBox="0 0 16 16"><circle cx="8" cy="8" r="7"/><path d="M1 8h14M8 1c2.5 2 2.5 12 0 14M8 1c-2.5 2-2.5 12 0 14" stroke="#fff" stroke-width="1" fill="none"/></svg>
          www.pineharbor.com
        </li>
      </ul>
    </div>
    <div class="address-band">Birchline Tower 2150 Meadow Crest Ave Suite 310</div>
  </section>

  <section class="card card-back">
    <div class="world-pattern" role="img" aria-label="Faint dotted world map pattern"></div>
    <div class="back-logo">
      <span class="logo-dot"></span>
      <span class="logo-name">PineHarbor</span>
    </div>
  </section>
</body>
</html>
```